Perfect — here’s the updated version of your description with **title #1** and the integration/booking functionality references removed, while still keeping the “motivation to book” idea in the design style:
---
**Luxury Property Website Design – Dominican Republic**
We are looking to create a professional and visually appealing **website design** for a premium property that we will be promoting as a short-term rental.
The property is located in an **exclusive area of the Dominican Republic** and offers a high-end experience for guests. Our goal is to create a website that highlights the **luxury, comfort, and exclusivity** of the property, while motivating visitors to **make a reservation inquiry**.
**Key Requirements:**
* A clean, modern, and elegant design that reflects the **premium nature** of the property.
* High-quality visual presentation of the **property’s best features** (rooms, amenities, location, views, nearby attractions).
* Easy-to-navigate structure
* Mobile-friendly and optimized for all screen sizes.
* Space for testimonials or guest reviews to build trust.
**Design Style We Like:**
* Elegant and sophisticated, with a touch of tropical luxury.
* Use of high-quality photography, subtle animations, and a warm color palette that reflects the Caribbean atmosphere.
* A premium feel, similar to boutique hotel or luxury villa rental websites.
**Deliverables:**
* Homepage design.
* Property detail page design (with gallery, amenities, and booking inquiry section).
Contact page or About Us page
* Photo Gallery
The final design should capture the essence of a **luxury getaway** and make visitors feel compelled to reserve their night.

```html
<!DOCTYPE html>
<html lang="en">
<head>
<meta charset="utf-8">
<title>Casa Serena – Luxury Villa</title>
<link href="https://fonts.googleapis.com/css2?family=Playfair+Display:wght@400;700;800&family=Inter:wght@400;500;600&display=swap" rel="stylesheet">
<style>
:root{
  --navy:#0d3a66;
  --navy-deep:#0a2f57;
  --coral:#f2645a;
  --cream:#fdf6ee;
  --white:#ffffff;
  --text:#3d4450;
  --field:#ececec;
}
*{box-sizing:border-box;margin:0;padding:0}
html,body{width:1200px;height:3989px;overflow:hidden}
body{background:var(--cream);font-family:"Inter",sans-serif;color:var(--text);position:relative}
.abs{position:absolute}
.btn{position:absolute;display:flex;align-items:center;justify-content:center;gap:14px;border-radius:22px;font-size:14px;font-weight:500;height:42px}
.btn .dot{width:14px;height:14px;border-radius:50%;background:currentColor;position:relative}
.btn .dot::after{content:"";position:absolute;left:5px;top:3px;border:4px solid transparent;border-left:5px solid var(--coral);border-right:0}
.btn.light .dot::after{border-left-color:var(--white)}
.btn.coral{background:var(--coral);color:var(--white)}
.btn.light{background:var(--white);color:var(--coral)}
.photo{position:absolute;border-radius:22px;overflow:hidden}

/* hero */
.hero{position:absolute;left:0;top:0;width:1200px;height:582px;background:linear-gradient(180deg,#3b4a63 0%,#c0764a 22%,#5a4a4a 34%,#1d3553 55%,#24527f 80%,#2d6aa0 100%)}
.nav{position:absolute;left:111px;top:57px;width:977px;height:82px;background:var(--white);border-radius:10px;display:flex;align-items:center;padding:0 38px}
.brand{font-family:"Inter",sans-serif;font-weight:600;font-size:26px;color:var(--navy);letter-spacing:1px}
.menu{margin-left:auto;display:flex;gap:37px;font-size:14.5px;color:#333}
.menu .active{color:var(--coral)}
.hero h1{position:absolute;left:0;width:1200px;top:208px;text-align:center;color:var(--white);font-family:"Playfair Display",serif;font-weight:800;font-size:68px;line-height:76px;letter-spacing:-1px}
.hero .lead{position:absolute;left:0;width:1200px;top:374px;text-align:center;color:var(--white);font-size:21px;font-weight:500}
.notch{position:absolute;left:530px;top:540px}

/* headings */
.h2{font-family:"Playfair Display",serif;font-weight:800;color:var(--navy);font-size:46px;letter-spacing:-.5px;line-height:1}
.h3{font-family:"Playfair Display",serif;color:var(--coral);font-size:27px;font-weight:400}

/* about */
.about-text{position:absolute;left:703px;top:752px;width:386px}
.about-text p{font-size:13px;line-height:26px;text-align:justify;margin-top:18px}
.cards{position:absolute;left:111px;top:1416px;display:flex;gap:17px}
.card{width:232px}
.card .photo{position:relative;height:320px;border:3px solid var(--white);box-shadow:0 4px 12px rgba(0,0,0,.12)}
.card p{text-align:center;font-size:15px;font-weight:500;color:#333;line-height:25px;margin-top:14px}

/* why */
.why{position:absolute;left:0;top:1879px;width:1200px;height:567px;background:linear-gradient(180deg,#1b3f6b,#0f3c74 60%,#0b3a72);color:var(--white);text-align:center}
.why .intro{position:absolute;left:260px;width:680px;top:175px;font-size:18px;line-height:30px}
.features{position:absolute;left:111px;top:287px;width:977px;display:flex}
.feature{width:244px;display:flex;flex-direction:column;align-items:center}
.feature .ic{width:86px;height:86px;border-radius:50%;background:var(--coral);display:flex;align-items:center;justify-content:center}
.feature h4{font-family:"Playfair Display",serif;font-weight:400;font-size:21px;margin-top:12px}
.feature p{font-size:14.5px;line-height:22px;margin-top:8px;width:200px}

/* testimonials */
.tcard{position:absolute;top:2655px;width:416px;height:201px;background:var(--white);border-radius:26px;box-shadow:0 6px 18px rgba(0,0,0,.06)}
.tcard q{position:absolute;left:85px;top:36px;width:290px;font-size:14px;line-height:26px;text-align:justify;quotes:"“ " " ”"}
.tcard .who{position:absolute;left:85px;top:158px;color:var(--coral);font-size:14.5px;font-weight:500}
.tcard .mark{position:absolute;right:22px;top:140px;font-family:"Playfair Display",serif;font-size:80px;line-height:1;color:#e3e3e3}
.avatar{position:absolute;width:106px;height:106px;border-radius:50%}

/* quote */
.quote{position:absolute;left:111px;top:2985px;width:977px;height:492px;background:var(--white);border-radius:26px;overflow:hidden;box-shadow:0 6px 18px rgba(0,0,0,.05)}
.field{position:absolute;left:474px;width:461px;height:50px;background:var(--field);border-radius:10px;display:flex;align-items:center;padding-left:28px;gap:12px;font-size:13.5px;color:#666}

/* footer */
.footer{position:absolute;left:0;top:3595px;width:1200px;height:394px;background:var(--navy-deep);color:var(--white)}
.fbrand{position:absolute;left:0;width:1200px;top:80px;text-align:center;font-family:"Inter",sans-serif;font-weight:600;font-size:40px;letter-spacing:1.5px;color:var(--white)}
.fnav{position:absolute;top:142px;left:0;width:1200px;display:flex;justify-content:center;gap:38px;font-size:15.5px;font-weight:600}
.rule{position:absolute;left:81px;width:1038px;height:1px;background:rgba(255,255,255,.25)}
.info{position:absolute;top:210px;display:flex;gap:18px;align-items:center;font-size:14px;line-height:24px}
.info .ic{width:40px;height:40px;border-radius:50%;background:var(--coral);display:flex;align-items:center;justify-content:center;flex:none}
.social{position:absolute;top:3895px;left:505px;display:flex;gap:16px}
.social span{width:38px;height:38px;border-radius:50%;background:var(--white)}
</style>
</head>
<body>

<section class="hero" role="img" aria-label="Infinity pool terrace overlooking the ocean at sunset">
  <nav class="nav">
    <div class="brand">CASA SERENA</div>
    <div class="menu"><span class="active">Home</span><span>About Us</span><span>Property</span><span>Gallery</span><span>Contact Us</span></div>
  </nav>
  <h1>Your Luxury Escape<br>in the Dominican Republic</h1>
  <p class="lead">A private Caribbean retreat for the discerning traveler.</p>
  <span class="btn coral" style="left:405px;top:421px;width:167px">Inquire Now <i class="dot" style="background:var(--white)"></i></span>
  <span class="btn light" style="left:602px;top:421px;width:193px">Book Your Stay <i class="dot" style="background:var(--coral)"></i></span>
  <svg class="notch" width="140" height="44" viewBox="0 0 140 44"><path d="M0 44 C30 44 35 2 70 2 C105 2 110 44 140 44Z" fill="#fdf6ee"/><circle cx="70" cy="37" r="12" fill="#0d3a66"/><path d="M70 29v14M65 38l5 5 5-5" stroke="#fff" stroke-width="1.8" fill="none"/></svg>
</section>

<div class="photo" role="img" aria-label="Wicker lounge chairs on a terrace beside palm trees and the sea" style="left:111px;top:712px;width:381px;height:413px;background:linear-gradient(160deg,#4f82b8,#8fb3d6 40%,#5f7a45 65%,#9a6a3e)"></div>
<div class="photo" role="img" aria-label="Modern white villa with infinity pool" style="left:285px;top:957px;width:316px;height:252px;border:4px solid var(--white);box-shadow:0 6px 16px rgba(0,0,0,.15);background:linear-gradient(180deg,#7fb2e3,#d9e6ef 45%,#e8e4dc 60%,#2a8fb8 80%,#1e6f92)"></div>
<div class="about-text">
  <div class="h2">WHO WE ARE</div>
  <div class="h3" style="margin-top:10px">The Essence of Luxury Living</div>
  <p>I must explain to you how all this mistaken idea of denouncing pleasure and praising pain was born and I will give you a complete account of the system, and expound the actual teachings of the great explorer of the truth, the master-builder of human happiness.</p>
  <p>No one rejects, dislikes, or avoids pleasure itself, because it is pleasure, but because those who do not know how to pursue pleasure</p>
</div>
<span class="btn coral" style="left:703px;top:1111px;width:162px">Explore More <i class="dot" style="background:var(--white)"></i></span>

<div class="abs h2" style="left:0;width:1200px;top:1307px;text-align:center">UNPARALLELED COMFORT &amp; STYLE</div>
<div class="abs h3" style="left:0;width:1200px;top:1357px;text-align:center">Experience True Caribbean Luxury</div>
<div class="cards">
  <div class="card"><div class="photo" role="img" aria-label="Infinity pool with city and ocean view" style="background:linear-gradient(180deg,#9cc7ec,#d6e2ea 45%,#3fb2cf 70%,#1a8fb3)"></div><p>Infinity Pool with Ocean<br>View</p></div>
  <div class="card"><div class="photo" role="img" aria-label="Designer interior with framed artwork" style="background:linear-gradient(180deg,#6a4e32,#e8dfcf 35%,#cfc2a6 75%,#b5a07d)"></div><p>Designer Interiors</p></div>
  <div class="card"><div class="photo" role="img" aria-label="Private chef plating a dish" style="background:linear-gradient(160deg,#d8d4cc,#f3f1ec 45%,#e6e2dc 70%,#bcb6ad)"></div><p>Private Chef &amp; Concierge<br>Service</p></div>
  <div class="card"><div class="photo" role="img" aria-label="Gated estate among trees at dusk" style="background:linear-gradient(180deg,#e9b98f,#b88e78 30%,#4a5e40 60%,#2f4a30)"></div><p>Exclusive Gated Location</p></div>
</div>

<section class="why" role="img" aria-label="Villa pool deck at dusk in deep blue tones">
  <div class="abs h2" style="left:0;width:1200px;top:72px;color:var(--white);font-size:44px">WHY STAY WITH US?</div>
  <div class="abs h3" style="left:0;width:1200px;top:125px;font-size:26px">Villa Highlights</div>
  <p class="intro">I must explain to you how all this mistaken idea of denouncing pleasure and praising pain was born and I will give you a complete account</p>
  <div class="features">
    <div class="feature"><div class="ic"><svg width="44" height="36" viewBox="0 0 44 36" fill="none" stroke="#fff" stroke-width="3"><path d="M4 4v28M4 24h36v8M4 18h36v6M10 18v-6h10v6"/></svg></div><h4>5 Bedrooms</h4><p>Generous bedrooms blending tropical charm with modern elegance.</p></div>
    <div class="feature"><div class="ic"><svg width="46" height="36" viewBox="0 0 46 36" fill="none" stroke="#fff" stroke-width="3"><path d="M4 28c6-4 10 4 16 0s10 4 16 0 6 0 6 0M6 20C8 8 24 2 32 12c-8-2-12 4-8 8"/></svg></div><h4>Oceanfront</h4><p>Where the sea becomes part of your everyday living space.</p></div>
    <div class="feature"><div class="ic"><svg width="36" height="42" viewBox="0 0 36 42" fill="#fff"><path d="M8 12a6 6 0 0 1 4-8 7 7 0 0 1 12 0 6 6 0 0 1 4 8z"/><rect x="10" y="14" width="16" height="10" rx="5"/><path d="M4 40c0-9 6-14 14-14s14 5 14 14z"/></svg></div><h4>Private Staff</h4><p>Enjoy the services of a dedicated chef, concierge, &amp; housekeeping team.</p></div>
    <div class="feature"><div class="ic"><svg width="44" height="42" viewBox="0 0 44 42" fill="none" stroke="#fff" stroke-width="3"><circle cx="22" cy="8" r="4"/><circle cx="10" cy="14" r="3"/><circle cx="34" cy="14" r="3"/><path d="M22 14v14M14 22l8 6 8-6M6 24c2 10 10 14 16 14s14-4 16-14"/></svg></div><h4>Gated Community</h4><p>Experience privacy, security, and true Caribbean tranquility.</p></div>
  </div>
</section>

<div class="abs h2" style="left:0;width:1200px;top:2538px;text-align:center">GUEST EXPERIENCES</div>
<div class="abs h3" style="left:0;width:1200px;top:2589px;text-align:center">Happy Customers</div>
<div class="tcard" style="left:164px"><q>I must explain to you how all this mistaken idea of denouncing pleasure and praising pain was born and I will give you a complete account</q><div class="who">Daniel &amp; Sofia M.</div><div class="mark">”</div></div>
<div class="avatar" role="img" aria-label="Guest portrait" style="left:111px;top:2703px;background:linear-gradient(135deg,#e7d9c6,#8a6a4d)"></div>
<div class="tcard" style="left:672px"><q>I must explain to you how all this mistaken idea of denouncing pleasure and praising pain was born and I will give you a complete account</q><div class="who">Daniel &amp; Sofia M.</div><div class="mark">”</div></div>
<div class="avatar" role="img" aria-label="Guest couple portrait" style="left:621px;top:2703px;background:linear-gradient(135deg,#dfe3e6,#9a7a5c)"></div>
<svg class="abs" style="left:575px;top:2890px" width="50" height="10"><circle cx="5" cy="5" r="4" fill="#0d3a66"/><circle cx="18" cy="5" r="4" fill="#bbb"/><circle cx="31" cy="5" r="4" fill="#bbb"/><circle cx="44" cy="5" r="4" fill="#bbb"/></svg>

<section class="quote">
  <div class="abs" role="img" aria-label="Hillside villa with terracotta roof, pool and sun loungers" style="left:0;top:0;width:428px;height:492px;background:linear-gradient(180deg,#5c8a3e,#c66a3e 30%,#e7ddcc 50%,#3a3a3a 75%,#22485e)"></div>
  <div class="abs h2" style="left:472px;top:36px">REQUEST A QUOTE</div>
  <div class="abs h3" style="left:472px;top:86px">Reserve Your Escape</div>
  <div class="field" style="top:142px"><svg width="12" height="12" viewBox="0 0 12 12" fill="#666"><circle cx="6" cy="3.5" r="3"/><path d="M0 12c0-4 3-5 6-5s6 1 6 5z"/></svg>Full Name</div>
  <div class="field" style="top:207px"><svg width="12" height="12" viewBox="0 0 12 12" fill="#666"><rect width="12" height="12" rx="2"/></svg>Phone Number</div>
  <div class="field" style="top:272px"><svg width="13" height="10" viewBox="0 0 13 10" fill="#666"><rect width="13" height="10" rx="1"/></svg>Email Address</div>
  <div class="field" style="top:337px"><svg width="14" height="11" viewBox="0 0 14 11" fill="none" stroke="#666" stroke-width="1.5"><ellipse cx="7" cy="5" rx="6" ry="4"/></svg>Comments</div>
  <span class="btn coral" style="left:759px;top:410px;width:176px">Send Message <i class="dot" style="background:var(--white)"></i></span>
</section>

<footer class="footer">
  <div class="fbrand">CASA SERENA</div>
  <div class="fnav"><span>Home</span><span>/</span><span>About Us</span><span>/</span><span>Property</span><span>/</span><span>Gallery</span><span>/</span><span>Contact Us</span></div>
  <div class="rule" style="top:195px"></div>
  <div class="info" style="left:81px"><span class="ic"><svg width="14" height="18" viewBox="0 0 14 18" fill="#fff"><path d="M7 0a7 7 0 0 1 7 7c0 5-7 11-7 11S0 12 0 7a7 7 0 0 1 7-7z"/><circle cx="7" cy="7" r="2.5" fill="#f2645a"/></svg></span><span>Avenida Coral 45, Playa Serena,<br>Dominican Republic</span></div>
  <div class="info" style="left:401px"><span class="ic"><svg width="16" height="16" viewBox="0 0 16 16" fill="#fff"><path d="M3 1l3 3-2 2c1 2 3 4 6 6l2-2 3 3-2 2C7 15 1 9 1 3z"/></svg></span><span>Phone Number:<br>+1 (555) 014-2290</span></div>
  <div class="info" style="left:648px"><span class="ic"><svg width="16" height="12" viewBox="0 0 16 12"><rect width="16" height="12" rx="1.5" fill="#fff"/><path d="M1 1l7 6 7-6" stroke="#f2645a" fill="none" stroke-width="1.5"/></svg></span><span>Email Address:<br>hello@casaserena-stays.com</span></div>
  <div class="info" style="left:908px"><span class="ic"><svg width="16" height="16" viewBox="0 0 16 16" fill="none" stroke="#fff" stroke-width="2"><circle cx="8" cy="8" r="7"/><path d="M8 4v4l3 2"/></svg></span><span>Hours<br>Mon – Sun: 9AM – 8PM</span></div>
  <div class="rule" style="top:274px"></div>
  <div class="abs" style="left:0;width:1200px;top:370px;text-align:center;font-size:12.5px">(C) Copyright 2025 | All Rights Reserved</div>
</footer>
<div class="social"><span></span><span></span><span></span><span></span></div>

</body>
</html>
```